Business Card Design Project

we need a business card design for our company: www.dravonix.ch
It's important to include our already existing logo (see website)

```html
<!DOCTYPE html>
<html lang="en">
<head>
<meta charset="utf-8">
<title>Dravonix Business Card</title>
<link rel="stylesheet" href="https://fonts.googleapis.com/css2?family=Arimo:wght@400;700&display=swap">
<style>
  :root {
    --brand-blue: #0070ba;
    --brand-blue-soft: #2a82c6;
    --paper: #ffffff;
    --ink-grey: #6a6a6a;
    --stage: #c4c4c4;
    --card-shadow: rgba(0, 0, 0, 0.28);
  }
  * { margin: 0; padding: 0; box-sizing: border-box; }
  html, body { width: 1200px; height: 900px; overflow: hidden; }
  body {
    background: var(--stage);
    font-family: "Arimo", Arial, sans-serif;
    position: relative;
  }
  .card {
    position: absolute;
    width: 498px;
    height: 283px;
    box-shadow: 3px 4px 8px var(--card-shadow);
  }

  /* Back side */
  .card-back {
    left: 556px;
    top: 147px;
    background: var(--brand-blue);
  }
  .card-back .brand-mark {
    position: absolute;
    left: 0; right: 0;
    top: 108px;
    text-align: center;
    font-size: 56px;
    font-weight: 700;
    letter-spacing: -1px;
    color: var(--brand-blue-soft);
  }
  .card-back .website {
    position: absolute;
    left: 0; right: 0;
    top: 216px;
    text-align: center;
    font-size: 16px;
    color: var(--paper);
    letter-spacing: 0.3px;
  }

  /* Front side */
  .card-front {
    left: 172px;
    top: 465px;
    background: var(--brand-blue);
  }
  .card-front .sheet {
    position: absolute;
    left: 20px; top: 20px;
    width: 459px; height: 244px;
    background: var(--paper);
  }
  .card-front .sheet-opening {
    position: absolute;
    left: 0; top: 71px;
    width: 498px; height: 142px;
    background: var(--paper);
  }
  .card-front .brand-name {
    position: absolute;
    left: 50px; top: 123px;
    font-size: 30px;
    font-weight: 700;
    letter-spacing: -0.5px;
    color: var(--brand-blue);
  }
  .contact {
    position: absolute;
    left: 229px; top: 60px;
    width: 240px;
    color: var(--ink-grey);
    font-size: 15px;
    line-height: 19.5px;
  }
  .contact .person-name {
    font-size: 17px;
    font-weight: 700;
    color: var(--brand-blue);
    line-height: 20px;
  }
  .contact .divider {
    height: 1px;
    margin: 8px 0 6px;
    background: linear-gradient(90deg, var(--brand-blue) 0%, var(--brand-blue) 70%, rgba(0,112,186,0) 100%);
  }
  .contact .channel {
    display: flex;
    align-items: center;
    gap: 7px;
  }
  .contact .channel svg { width: 13px; height: 13px; flex: none; }
</style>
</head>
<body>

  <section class="card card-back" aria-label="Business card back">
    <div class="brand-mark">Dravonix</div>
    <div class="website">www.dravonix.ch</div>
  </section>

  <section class="card card-front" aria-label="Business card front">
    <div class="sheet"></div>
    <div class="sheet-opening"></div>
    <div class="brand-name">Dravonix</div>

    <div class="contact">
      <div class="person-name">Lena Marti</div>
      <div class="role">Co-Founder</div>
      <div class="divider"></div>
      <div class="address">Falkenweg 17<br>8005 Zürich</div>
      <div class="divider"></div>
      <div class="channel">
        <svg viewBox="0 0 13 13" aria-hidden="true"><path d="M3 1 L5 1 L5.6 4 L4.3 5 Q5.4 7.6 8 8.7 L9 7.4 L12 8 L12 10 Q11.5 12 9.5 12 Q2 11 1 3.5 Q1 1.5 3 1 Z" fill="var(--brand-blue)"/></svg>
        <span>+41 44 318 60 40</span>
      </div>
      <div class="channel">
        <svg viewBox="0 0 13 13" aria-hidden="true"><rect x="0.8" y="2.5" width="11.4" height="8" fill="none" stroke="var(--brand-blue)" stroke-width="1"/><path d="M0.8 2.5 L6.5 7 L12.2 2.5" fill="none" stroke="var(--brand-blue)" stroke-width="1"/></svg>
        <span>hello@dravonix.ch</span>
      </div>
      <div class="channel">
        <svg viewBox="0 0 13 13" aria-hidden="true"><circle cx="6.5" cy="6.5" r="5.5" fill="var(--brand-blue)"/></svg>
        <span>dravonix.ch</span>
      </div>
    </div>
  </section>

</body>
</html>
```